Anzeigengestaltung für Darstellung der Zentralaussagen einer PR-Agentur
Zielgruppe
Wir suchen ein hochwertiges und anspechendes Design für eine halbseitige (DIN A5) Werbeanzeige, um Insolvenzverwalter auf unsere PR-Arbeit für ihre eignenen Insolvenzfälle aufmerksam zu machen. Idealerweise übernimmt der Insolvenzverwalter also die rechtlichen Aufgaben innerhalb der Insolvenz und wir die kommunikativen, also die Öffentlichkeitsarbeit und interne Kommunikation. Meist schätzen die Anwälte hierbei dann unser breites Netzwerk (zu Journalisten etc.), unser Kommunikationsgefühl und, dass wir zudem rechtliches Verständnis mitbringen.
Unsere Zielgruppe sind somit Anwälte, die im Insolvenzrecht tätig sind, also als Insolvenzverwalter arbeite, sowie Unternehmen, denen eine Insolvenz droht oder sich in einer Insolvenz befinden.
Wir sind eine PR-Agenur, spezialisiert auf das juristische Umfeld. Wir beraten Unternehmen und Anwaltskanzleien, wie sie in Rechtsstreitigkeiten mit der Öffentlihkeit umgehen. Spezialisiert sind wir auf die Insolvenzkommunikation. Hier beraten wir die Insolvenzverwaltung und das von der Insolvenz betroffene Unternehmen in der internen und externen Kommunikation. Hierbei bringen wir als Unternehmen mit unseren Mitarbeitern Fachkenntnisse aus PR, sowie juristische Expertise mit, denn alle unsere Berater haben einen juristischen Abschluss. In einer juristischen Ausnahmesituation wie einer Insolvenz ist es für uns daher leicht, den Sachverhalt zu erfassen. Das hebt uns von anderen PR-Agenturen ab. Wir kümmern uns um alle kommunikativen Fragen, die innerhalb des Unternehmens während der Insolvenz auftreten und um Medienanfragen rund um die Insolvenz von außerhalb (klassische Presseanfragen). Verschwiegenheit und Diskretion gegenüber unserem Mandanten steht für uns dabei stets mit an oberster Stelle.
Aufgabenstellung
Wir möchten die Anzeige möglichst klassisch und seriös halten. Trotzdem sollte sie ins Auge fallen und herausstechen. Visuell sollte sie ansprechend sein und mit symbolhaften Bildern unterstrichen, da wir selbst als Berater nicht in der Anzeige abgebildet sein wollen. Textlich sollte es einen nicht erschlagen. Unsere Hauptdienstleistungen und Zentralaussagen sollten aber drin sein (juristische und kommunikative Expertise, interne und externe Insolvenzkommunikation, kein Ein-Mann-Betrieb, gut vernetzt)

```html
<!DOCTYPE html>
<html lang="de">
<head>
<meta charset="utf-8">
<title>CLARIS – Anzeige Insolvenzkommunikation</title>
<link rel="stylesheet" href="https://fonts.googleapis.com/css2?family=Cinzel:wght@400;500&family=Roboto:wght@300;400&family=Open+Sans:wght@500&display=swap">
<style>
  :root {
    --stage: #e4e4e4;
    --night: #0b0b0b;
    --gold: #a5881a;
    --gold-text: #b39227;
    --ink: #222222;
    --logo-ink: #333333;
    --paper: #ffffff;
  }
  * { box-sizing: border-box; margin: 0; padding: 0; }
  html, body { width: 1200px; height: 1050px; overflow: hidden; }
  body { background: var(--stage); position: relative; }

  .ad {
    position: absolute; left: 0; top: 103px;
    width: 1200px; height: 843px;
    background: var(--paper);
  }
  .hero {
    position: absolute; left: 0; top: 0; width: 1200px; height: 541px;
    background:
      radial-gradient(ellipse 420px 160px at 560px 470px, rgba(170,170,170,.55), rgba(60,60,60,0) 70%),
      radial-gradient(ellipse 300px 220px at 380px 430px, rgba(120,120,120,.35), rgba(0,0,0,0) 70%),
      linear-gradient(180deg, #050505 0%, #1a1a1a 30%, #0d0d0d 60%, #2b2b2b 88%, #141414 100%);
  }
  .hero-shade {
    position: absolute; left: 0; top: 523px; width: 1200px; height: 18px;
    background: linear-gradient(90deg, #1a1a12, #3b3512 50%, #1a1a12);
  }
  .headline {
    position: absolute; left: 0; top: 82px; width: 1200px;
    text-align: center; color: #fff;
    font-family: "Cinzel", serif; font-weight: 400;
    font-size: 57px; line-height: 66px; letter-spacing: 0.045em;
  }
  .tagline {
    position: absolute; left: 471px; top: 250px;
    color: var(--gold-text);
    font-family: "Roboto", sans-serif; font-weight: 300;
    font-size: 23px; line-height: 29px;
  }
  .hotline {
    position: absolute; left: 924px; top: 318px; width: 230px; height: 110px;
  }
  .hotline-text {
    position: absolute; left: 70px; top: 22px;
    color: #fff; font-family: "Open Sans", sans-serif; font-weight: 500;
    font-size: 17px; line-height: 23px;
    transform: rotate(-8deg); transform-origin: left top;
  }
  .band-top { position: absolute; left: 0; top: 541px; width: 1200px; height: 19px; background: var(--gold); }
  .band-bottom { position: absolute; left: 0; top: 831px; width: 1200px; height: 12px; background: var(--gold); }

  .copy {
    position: absolute; top: 603px; width: 347px;
    color: var(--ink); font-family: "Roboto", sans-serif; font-weight: 300;
    font-size: 14px; line-height: 20.2px;
    text-align: justify; hyphens: auto;
  }
  .copy-left { left: 55px; }
  .copy-right { left: 427px; }

  .brand {
    position: absolute; left: 796px; top: 666px;
    color: var(--logo-ink); font-family: "Cinzel", serif; font-weight: 400;
    font-size: 54px; line-height: 56px; letter-spacing: 0.06em;
  }
  .contact {
    position: absolute; left: 0; top: 770px; width: 1200px;
    text-align: center; color: var(--ink);
    font-family: "Roboto", sans-serif; font-weight: 300;
    font-size: 14px; line-height: 20.5px;
  }
  .contact .sep { color: var(--gold); margin: 0 6px; }
</style>
</head>
<body>
  <article class="ad">
    <div class="hero" role="img" aria-label="Schwarzweißfoto: weißer Springer steht auf einem Schachbrett neben einem umgefallenen schwarzen König"></div>
    <div class="hero-shade"></div>

    <h1 class="headline">Wir nehmen alle Hürden<br>der Insolvenzkommunikation</h1>

    <p class="tagline">Wir kommunizieren für unsere Mandanten<br>Rechts- und Krisenthemen auf höchstem Niveau</p>

    <div class="hotline">
      <svg width="230" height="110" viewBox="0 0 230 110" aria-hidden="true">
        <line x1="2" y1="26" x2="218" y2="0" stroke="var(--gold)" stroke-width="2"/>
        <line x1="14" y1="110" x2="228" y2="82" stroke="var(--gold)" stroke-width="2"/>
        <path d="M16 42 c-6 4 -8 10 -4 18 c6 12 16 24 30 32 c6 3 10 2 13 -2 l2 -3 c1 -2 0 -4 -2 -5 l-8 -5 c-2 -1 -4 -1 -5 1 l-3 3 c-8 -4 -14 -12 -18 -20 l3 -3 c2 -1 2 -3 1 -5 l-5 -9 c-1 -2 -3 -3 -5 -2 z"
              fill="none" stroke="#fff" stroke-width="2.2" stroke-linejoin="round"/>
      </svg>
      <p class="hotline-text">24-Stunden-<br>Krisenhotline<br>0800 312 312 5</p>
    </div>

    <div class="band-top"></div>

    <p class="copy copy-left">Seit Jahren verantworten wir die Medienarbeit ausschließlich im juristischen Umfeld: von der Regelinsolvenz bis zur Eigenverwaltung haben wir bereits einige Insolvenzen kommunikativ begleitet. Unser Ansatz: Recht und Kommunikation müssen gemeinsam gedacht werden. Ob intern oder extern – wir entlasten Sie in allen PR-Fragen.</p>

    <p class="copy copy-right">Bei CLARIS beraten ausschließlich Medienexperten mit einem juristischen Abschluss. Wir haben unter anderem für Meinungsführerredaktionen wie die MORGEN-Zeitung, FAKTUM Online und den TAGESBLATT gearbeitet und können somit auf ein breites Netzwerk zurückgreifen. Unsere rechtliche und kommunikative Erfahrung ist die Basis für eine erfolgreiche Insolvenzkommunikation.</p>

    <div class="brand">CLARIS</div>

    <address class="contact" style="font-style: normal;">
      CLARIS Rechtskommunikation GmbH<span class="sep">|</span>Lindenallee 12<span class="sep">|</span>48143 Münster<span class="sep">|</span>Tel.: +49 251 55 43 210<br>
      post@claris.media<span class="sep">|</span>www.claris-media.de
    </address>

    <div class="band-bottom"></div>
  </article>
</body>
</html>
```